Brindle Logistics Business Card Design

We are a trucking and warehousing company. We run freight in the US manly from the Pacific NW to TX and back up the the PNW. We also do warehousing where we store, move, and distribute freight. Looking for a clean and modern design of business card. We would like to look rich and elegant. Attached is our logo.

Industry/Entity Type

Trucking Company

Contact Information for Business Card

Looking for a clean and modern design of business card. We would like to look rich and elegant.

Font styles to use
Sans Serif

Colors

Designer to choose colors to be used in the design.

Requirements
Must have
• logo but it should not dominate the card
Should not have
• logo should not dominate the card

```html
<!DOCTYPE html>
<html lang="en">
<head>
<meta charset="utf-8">
<title>Brindle Logistics Business Card</title>
<link href="https://fonts.googleapis.com/css2?family=Roboto:wght@400;500;700&display=swap" rel="stylesheet">
<style>
  :root {
    --backdrop: #3a3a3a;
    --card: #262627;
    --white: #ffffff;
    --blue: #0a63b0;
    --orange: #f0921c;
    --grey: #9a9a9a;
    --muted: #d8d8d8;
  }
  * { box-sizing: border-box; margin: 0; padding: 0; }
  html, body { width: 799px; height: 1200px; overflow: hidden; }
  body {
    background: var(--backdrop);
    font-family: "Roboto", Arial, sans-serif;
    display: flex;
    flex-direction: column;
    align-items: center;
    justify-content: space-around;
    padding: 60px 0;
  }
  .card {
    position: relative;
    width: 620px;
    height: 354px;
    background: var(--card);
    border-radius: 24px;
    overflow: hidden;
    box-shadow: 0 14px 30px rgba(0,0,0,.45);
  }

  /* Front */
  .brand {
    position: absolute;
    left: 0; right: 0; top: 120px;
    display: flex;
    align-items: center;
    justify-content: center;
    gap: 16px;
  }
  .brand-dot {
    width: 30px; height: 30px;
    border-radius: 50%;
    background: var(--blue);
  }
  .brand-name {
    color: var(--white);
    font-weight: 500;
    font-size: 40px;
    letter-spacing: 2px;
    text-transform: uppercase;
  }
  .front .web {
    position: absolute;
    left: 0; right: 0; top: 256px;
    text-align: center;
    color: var(--white);
    font-size: 16px;
  }
  .accent-line {
    position: absolute;
    top: 266px;
    height: 2px;
    width: 90px;
    background: var(--blue);
  }
  .accent-line.left { left: 70px; }
  .accent-line.right { right: 70px; }
  .stripe {
    position: absolute;
    left: 0; right: 0; bottom: 0;
    height: 14px;
    display: flex;
  }
  .stripe .seg-blue { flex: 0 0 34%; background: var(--blue); }
  .stripe .seg-orange { flex: 0 0 36%; background: var(--orange); }
  .stripe .seg-grey { flex: 1; background: var(--grey); }

  /* Back */
  .back .brand-small {
    position: absolute;
    left: 36px; top: 34px;
    display: flex;
    align-items: center;
    gap: 10px;
  }
  .back .brand-small .brand-dot { width: 20px; height: 20px; }
  .back .brand-small .brand-name { font-size: 28px; letter-spacing: 1.5px; }
  .person {
    position: absolute;
    left: 36px; top: 112px;
  }
  .person-name {
    color: var(--blue);
    font-weight: 700;
    font-size: 26px;
  }
  .person-title {
    color: var(--white);
    font-size: 14px;
    margin-top: 2px;
  }
  .contacts {
    position: absolute;
    left: 36px; top: 196px;
    list-style: none;
    color: var(--white);
    font-size: 15px;
  }
  .contacts li {
    display: flex;
    align-items: center;
    gap: 10px;
    height: 23px;
  }
  .contacts svg { width: 13px; height: 13px; fill: var(--muted); flex: 0 0 13px; }
  .address {
    position: absolute;
    left: 36px; top: 272px;
    color: var(--white);
    font-size: 15px;
  }
  .emblem-area {
    position: absolute;
    right: 0; top: 90px;
    width: 250px; height: 264px;
    border-top-left-radius: 140px;
    background: radial-gradient(circle at 60% 40%, rgba(10,99,176,.55), rgba(10,99,176,.15) 70%);
  }
</style>
</head>
<body>

  <section class="card front">
    <div class="brand">
      <span class="brand-dot"></span>
      <span class="brand-name">Brindle Logistics, LLC</span>
    </div>
    <span class="accent-line left"></span>
    <p class="web">www.brindlelogisticsllc.com</p>
    <span class="accent-line right"></span>
    <div class="stripe">
      <span class="seg-blue"></span><span class="seg-orange"></span><span class="seg-grey"></span>
    </div>
  </section>

  <section class="card back">
    <div class="brand-small">
      <span class="brand-dot"></span>
      <span class="brand-name">Brindle Logistics, LLC</span>
    </div>
    <div class="person">
      <p class="person-name">Daniel Morrow</p>
      <p class="person-title">Managing Director</p>
    </div>
    <ul class="contacts">
      <li>
        <svg viewBox="0 0 24 24"><path d="M6.6 10.8a15.1 15.1 0 0 0 6.6 6.6l2.2-2.2a1 1 0 0 1 1-.25 11.4 11.4 0 0 0 3.6.57 1 1 0 0 1 1 1V20a1 1 0 0 1-1 1A17 17 0 0 1 3 4a1 1 0 0 1 1-1h3.5a1 1 0 0 1 1 1c0 1.25.2 2.45.57 3.57a1 1 0 0 1-.25 1z"/></svg>
        555 0142 318
      </li>
      <li>
        <svg viewBox="0 0 24 24"><path d="M2 5h20v14H2zm2 2v.5l8 5 8-5V7zm0 2.8V17h16V9.8l-8 5z"/></svg>
        daniel@brindlelogisticsllc.com
      </li>
      <li>
        <svg viewBox="0 0 24 24"><path d="M12 2a10 10 0 1 0 0 20 10 10 0 0 0 0-20zm0 2c.9 0 2.2 1.8 2.8 5H9.2C9.8 5.8 11.1 4 12 4zM4.3 11h4.8a18 18 0 0 0 0 2H4.3a8 8 0 0 1 0-2zm6.8 0h1.8v2h-1.8zm3.8 0h4.8a8 8 0 0 1 0 2h-4.8a18 18 0 0 0 0-2zM9.2 15h5.6c-.6 3.2-1.9 5-2.8 5s-2.2-1.8-2.8-5z"/></svg>
        www.brindlelogisticsllc.com
      </li>
    </ul>
    <p class="address">2418 Harbor View Road, Tacoma, WA 98421</p>
    <div class="emblem-area" role="img" aria-label="Area reserved for the company emblem"></div>
  </section>

</body>
</html>
```